Red Sea Boat trips in need of Business Card for Private Boat Tours

We need a Business card for a new business set-up in Egypt on the Red Sea for private snorkelling and boat excursions to one of the world's most beautiful reefs. We have wording logo already set-up which matches the boat but we need business cards to be bright and colourful with pictures of boat

Industry/Entity Type

Tourism

Contact Information for Business Card

Two Silver Gulls (font provided) Boat Trips

```html
<!DOCTYPE html>
<html lang="en">
<head>
<meta charset="utf-8">
<title>Two Silver Gulls – Business Card</title>
<link rel="stylesheet" href="https://fonts.googleapis.com/css2?family=Mulish:wght@400;600;800&family=Kaushan+Script&display=swap">
<style>
  :root {
    --page-bg: #e9e6e1;
    --card-white: #ffffff;
    --ink: #111111;
    --ink-soft: #4a4a4a;
    --accent-blue: #1f9fe0;
    --sea-deep: #1f6f93;
    --sea-light: #6fb8d2;
    --sky: #dfe9ee;
    --canopy: #1e2f6b;
    --reef-dark: #141414;
    --reef-mid: #3a3a3a;
    --reef-light: #9a9a9a;
  }
  * { box-sizing: border-box; margin: 0; padding: 0; }
  html, body { width: 1200px; height: 900px; overflow: hidden; }
  body {
    background: var(--page-bg);
    font-family: "Mulish", sans-serif;
    position: relative;
  }
  .card {
    position: absolute;
    overflow: hidden;
    box-shadow: 0 10px 30px rgba(0,0,0,0.18);
    background: var(--card-white);
  }
  /* Front card */
  .card-front { left: 60px; top: 290px; width: 580px; height: 330px; }
  .front-photo {
    position: absolute; inset: 0 0 0 120px;
    background:
      linear-gradient(180deg, var(--sky) 0%, #cfd9dc 30%, var(--sea-light) 48%, var(--sea-deep) 100%);
  }
  .front-photo .canopy-tone {
    position: absolute; left: 45%; top: 42%; width: 45%; height: 40%;
    background: radial-gradient(ellipse at center, #e9eef2 0%, rgba(233,238,242,0) 70%);
  }
  .front-fade {
    position: absolute; inset: 0;
    background: linear-gradient(90deg, #ffffff 0%, #ffffff 22%, rgba(255,255,255,0.85) 38%, rgba(255,255,255,0) 60%);
  }
  .brand-name {
    position: absolute; right: 28px; top: 28px;
    font-family: "Mulish", sans-serif; font-weight: 800;
    font-size: 30px; color: var(--ink); letter-spacing: 0.5px;
  }
  .contact-block { position: absolute; left: 36px; bottom: 40px; }
  .person-name {
    font-family: "Kaushan Script", cursive; color: var(--accent-blue);
    font-size: 28px; line-height: 1;
  }
  .person-role { color: var(--ink-soft); font-size: 15px; margin: 4px 0 12px; }
  .contact-row {
    display: flex; align-items: center; gap: 8px;
    font-size: 14px; color: #222; margin-bottom: 5px;
  }
  .contact-row svg { width: 13px; height: 13px; fill: var(--accent-blue); flex: none; }
  .address-block {
    position: absolute; left: 270px; bottom: 104px;
    border-left: 2px solid var(--accent-blue);
    padding-left: 12px; font-size: 14px; color: #222; line-height: 1.3;
  }
  /* Back card */
  .card-back { left: 720px; top: 160px; width: 340px; height: 590px; background: var(--reef-dark); }
  .back-photo {
    position: absolute; inset: 0;
    background:
      radial-gradient(ellipse at 70% 12%, var(--reef-light) 0%, rgba(154,154,154,0) 45%),
      radial-gradient(ellipse at 40% 60%, var(--reef-mid) 0%, rgba(58,58,58,0) 60%),
      linear-gradient(160deg, #555 0%, var(--reef-dark) 55%, #0d0d0d 100%);
  }
  .back-brand {
    position: absolute; left: 0; right: 0; top: 250px;
    text-align: center; font-family: "Mulish", sans-serif; font-weight: 800;
    font-size: 30px; color: var(--card-white);
  }
</style>
</head>
<body>
  <section class="card card-front">
    <div class="front-photo" role="img" aria-label="Photo of a white motor boat with a navy canopy moored in a Red Sea marina, resort buildings and palms behind">
      <div class="canopy-tone"></div>
    </div>
    <div class="front-fade"></div>
    <div class="brand-name">Two Silver Gulls</div>

    <div class="address-block">
      <div>00 dummy city</div>
      <div>dummy place 0000</div>
    </div>

    <div class="contact-block">
      <div class="person-name">Adam Carter</div>
      <div class="person-role">Director</div>
      <div class="contact-row">
        <svg viewBox="0 0 24 24"><path d="M6.6 10.8a15.1 15.1 0 0 0 6.6 6.6l2.2-2.2a1 1 0 0 1 1-.25 11.4 11.4 0 0 0 3.6.57 1 1 0 0 1 1 1V20a1 1 0 0 1-1 1A17 17 0 0 1 3 4a1 1 0 0 1 1-1h3.5a1 1 0 0 1 1 1c0 1.25.2 2.45.57 3.57a1 1 0 0 1-.25 1z"/></svg>
        <span>555-210-4870</span>
      </div>
      <div class="contact-row">
        <svg viewBox="0 0 24 24"><path d="M2 5h20v14H2z M2 5l10 8 10-8" fill="none" stroke="#1f9fe0" stroke-width="2.5"/></svg>
        <span>info@twosilvergulls.com</span>
      </div>
      <div class="contact-row">
        <svg viewBox="0 0 24 24"><circle cx="12" cy="12" r="9" fill="none" stroke="#1f9fe0" stroke-width="2"/><path d="M3 12h18M12 3c3 3 3 15 0 18M12 3c-3 3-3 15 0 18" fill="none" stroke="#1f9fe0" stroke-width="1.6"/></svg>
        <span>www.twosilvergulls.com</span>
      </div>
    </div>
  </section>

  <section class="card card-back">
    <div class="back-photo" role="img" aria-label="Black and white underwater photo of two snorkellers with long fins swimming above a coral reef"></div>
    <div class="back-brand">Two Silver Gulls</div>
  </section>
</body>
</html>
```